Law Office needs stationery design and business card

I currently have been using the same letterhead for the last 8 years. Since i 'm about to adding another location, I want to revamp my letterhead and business card. I already have a logo i'm happy with. I will upload my current letterhead, fax sheet, envelope, and logos. I need a business card also. I have 2 locations, 1 phone number, 1 fax line, website, etc. If possible and fitting with the design, I would like to keep the same information listed currently on the letterhead.

**Keep in mind, I also NEED A FAX SHEET COVER. thank you
Updates

Hello, Please submit a Gray Scale or Black and White version of your designs also, since most of the time I will be printing NON color stationery. I will seldom use a color print for my letterhead, I would like to have a color version for my benefit, however i will print in grayscale majority of the time . For the Business Card, that can just be in color. When I get my business cards they will be in color.Thank youEnrique Added Sunday, September 18, 2016

Industry/Entity Type

Business

```html
<!DOCTYPE html>
<html lang="en">
<head>
<meta charset="utf-8">
<title>Marvell Law Stationery</title>
<link href="https://fonts.googleapis.com/css2?family=EB+Garamond:ital,wght@0,400;0,600;1,400&family=Archivo+Black&display=swap" rel="stylesheet">
<style>
:root{
  --gold:#b9a35c;
  --ink:#1b1b1b;
  --paper:#ffffff;
  --backdrop:#e9e4da;
  --text:#2a2a2a;
}
*{box-sizing:border-box;margin:0;padding:0}
html,body{width:1200px;height:1200px;overflow:hidden}
body{background:var(--backdrop);position:relative;font-family:"EB Garamond",Georgia,serif;color:var(--text)}
.sheet{position:absolute;background:var(--paper)}
.letterhead{left:75px;top:117px;width:510px;height:659px}
.fax-sheet{left:628px;top:117px;width:511px;height:657px}
.envelope{left:65px;top:849px;width:520px;height:259px}
.business-card{left:798px;top:918px;width:211px;height:120px;overflow:hidden}
.brand{position:absolute;display:flex;align-items:center;gap:7px;font-weight:600;color:var(--ink);letter-spacing:1.5px;white-space:nowrap}
.brand-mark{width:14px;height:14px;background:var(--gold)}
.rule{position:absolute;left:0;right:0;height:4px;border-top:1px solid var(--gold);border-bottom:1px solid var(--gold)}
.addresses{position:absolute;left:378px;top:33px;font-size:7.5px;line-height:9.5px;color:var(--gold)}
.addresses p+p{margin-top:10px}
.contact-line{position:absolute;left:0;right:0;text-align:center;font-size:7.5px;color:var(--text)}
.contact-line b{color:var(--gold);font-weight:400}
.dot{display:inline-block;width:7px;height:7px;border-radius:50%;background:var(--gold);vertical-align:-1px;margin-right:3px}
.attorneys{position:absolute;left:0;right:0;text-align:center;font-size:7.5px;line-height:10px}
.attorneys i{font-style:italic}
.fax-title{position:absolute;left:36px;top:30px;font-family:"Archivo Black",Arial,sans-serif;font-size:40px;letter-spacing:1px;color:#000}
.card-band{position:absolute;left:0;top:0}
.card-name{position:absolute;left:78px;top:68px;font-size:6.5px;font-weight:600;color:var(--ink);letter-spacing:.3px}
.card-name span{color:var(--gold)}
.card-info{position:absolute;left:62px;top:83px;font-size:4.2px;line-height:5.6px;color:var(--text)}
.card-info b{color:var(--gold);font-weight:400}
</style>
</head>
<body>

<section class="sheet letterhead">
  <div class="brand" style="left:42px;top:86px;font-size:15px"><span class="brand-mark"></span>MARVELL LAW</div>
  <div class="addresses">
    <p>• 214 Linden Ave.,<br>Suite 300, Fairview, PA 19060</p>
    <p>• 518 Maple St.,<br>Brookdale, PA 19015</p>
  </div>
  <div class="rule" style="top:112px"></div>
  <div class="contact-line" style="top:606px"><b>T</b> 610.555.0142 &nbsp;<b>F</b> 484.555.0187 &nbsp;<b>|</b> www.MarvellLaw.com &nbsp;<span class="dot"></span>MarvellLaw</div>
  <div class="rule" style="top:618px"></div>
  <div class="attorneys" style="top:624px">Tobias Marvell Esq. | <i>Tobias@MarvellLaw.com</i> • Dana Whitcomb Esq. | <i>Dana@MarvellLaw.com</i><br>Clara Benton Esq. | <i>Clara@MarvellLaw.com</i> • Owen Hartley Esq. of counsel | <i>Owen@MarvellLaw.com</i></div>
</section>

<section class="sheet fax-sheet">
  <div class="fax-title">FAX</div>
  <div class="brand" style="left:180px;top:76px;font-size:15px"><span class="brand-mark"></span>MARVELL LAW</div>
  <div class="rule" style="top:103px"></div>
  <div class="contact-line" style="top:596px"><b>T</b> 610.555.0142 &nbsp;<b>F</b> 484.555.0187 &nbsp;<b>|</b> www.MarvellLaw.com &nbsp;<span class="dot"></span>MarvellLaw</div>
  <div class="rule" style="top:608px"></div>
  <div class="attorneys" style="top:614px">Tobias Marvell Esq. | <i>Tobias@MarvellLaw.com</i> • Dana Whitcomb Esq. | <i>Dana@MarvellLaw.com</i><br>Clara Benton Esq. | <i>Clara@MarvellLaw.com</i> • Owen Hartley Esq. of counsel | <i>Owen@MarvellLaw.com</i></div>
</section>

<section class="sheet envelope">
  <div class="brand" style="left:24px;top:60px;font-size:14px"><span class="brand-mark"></span>MARVELL LAW</div>
  <div class="rule" style="top:82px"></div>
</section>

<section class="sheet business-card">
  <svg class="card-band" width="30" height="120" viewBox="0 0 30 120" aria-hidden="true">
    <polygon points="0,0 24,0 24,56 0,44" fill="var(--ink)"/>
    <polygon points="0,50 24,62 24,120 0,120" fill="var(--gold)"/>
  </svg>
  <div class="brand" style="left:84px;top:38px;font-size:7px;gap:4px;letter-spacing:.8px"><span class="brand-mark" style="width:7px;height:7px"></span>MARVELL LAW</div>
  <div class="rule" style="top:58px;left:24px;height:3px"></div>
  <div class="card-name">TOBIAS MARVELL <span>ESQ.</span></div>
  <div class="card-info">
    <b>T</b> 610.555.0142 &nbsp;<b>F</b> 484.555.0187 &nbsp;<b>●</b> MarvellLaw<br>
    <b>E</b> Tobias@MarvellLaw.com &nbsp;<b>|</b> www.MarvellLaw.com<br>
    &nbsp;&nbsp;214 Linden Ave., Suite 300, Fairview, PA 19060<br>
    &nbsp;&nbsp;518 Maple St., Brookdale, PA 19015
  </div>
</section>

</body>
</html>
```